Corporate Design für Homöopathische Familienpraxis Mareike Sonnfeld-Brandt
Zielgruppe
Ich bin Heilpraktikerin und Homöopathin
- ich behandel in meiner Praxis ganzheitlich und Patienten jeden Alters
- besonderer Augenmerk liegt dabei auf Schwangere, Säuglinge und Kinder
Aufgabenstellung
Ich möchte gern eine recht breite Zielgruppe ansprechen
- natürlich aber nicht zu sehr öko
- weiblich aber nicht kitschig
- Kinder und Erwachsene gleichermaßen
- naturheilkunde aber keine Esotherik
- modern aber nicht zu kühl
- klassisch aber nicht spießig
Die Grafik der Seerose ist eine Zeichnung von mir und aus ihr soll mein Logo entstehen.
Wichtig dabei ist, dass sich die pinke Seerose IN einem Wassertropfen befindet. Dieser steht symbolisch für die Schwangerschaft/Gebärmutter, als auch die Ganzheitlichkeit (Körper/Geist/Seele), als auch die gesamte Familie.
Form, Blütenblätter und -anzahl dürfen gern verändert werden.
Aus meinem Titel soll deutlich werden, dass es sich um meine Praxis und nicht um eine Praxisgemeinschaft handelt.
Familienpraxis steht für die ganze Familie.
Es gibt bereits eine gesicherte Domain: tautropfen-hausheilkunde.de, diese ist jedoch zu lang und es bedarf einer einprägsamen und pfiffigen Lösung.
Auch für das Erstellen meiner Homepage suche ich noch jemanden und bin gerne für Vorschläge und Angebote offen.
Meine Überlegung war es, diese mittels Wordpress zu erstellen.
Selbstverständlich angepasst an das hier entstandene CD.
Meine Grundidee war es, den Titel: "Homöopathische Familienpraxis Mareike Sonnfeld-Brandt"
in einer Art Schreibschrift abzubilden und als weitere Schriftart für alle Texte eine sehr geradlinige und moderne Schriftart zu verwenden.
Die Schriftfarbe, vor allem die der Fließtexte, gern in grau, evtl. auch dunkelblau, jedoch kein schwarz, da die Seerose sehr farbig ist, darf der Rest der Gestaltung eher schlicht gehalten werden.
Auch hier freue ich mich über Vorschläge dazu und gänzlich neue Ideen.
Das Logo sollte von seiner Aufmachung her so gebaut sein, dass es sowohl sehr klein (Briefkopf), als auch sehr groß (Werbefläche) verwendet werden kann.
Wichtig sind vor allem das Logo..

```html
<!DOCTYPE html>
<html lang="de">
<head>
<meta charset="utf-8">
<title>Corporate Design – Homöopathische Familienpraxis Mareike Sonnfeld-Brandt</title>
<link href="https://fonts.googleapis.com/css2?family=Barlow:wght@300;400;600&family=Oswald:wght@400&display=swap" rel="stylesheet">
<style>
  :root {
    --pink: #d1669f;
    --grey-swatch: #a9a9ae;
    --text: #7a7a7e;
    --text-strong: #8a8a8e;
    --rule: #c8c8cc;
    --stage: #d6d6da;
    --paper: #ffffff;
    --emboss-light: #c9c9c9;
  }
  * { margin: 0; padding: 0; box-sizing: border-box; }
  html, body { width: 1200px; height: 2698px; overflow: hidden; }
  body {
    position: relative;
    background: var(--paper);
    font-family: "Barlow", Arial, sans-serif;
    font-weight: 300;
    color: var(--text);
  }
  .abs { position: absolute; }

  /* colour swatches */
  .swatch { position: absolute; top: 28px; width: 30px; height: 13px; }
  .swatch--pink { left: 28px; background: var(--pink); }
  .swatch--grey { left: 71px; background: var(--grey-swatch); }

  /* brand lockup: plain circle + practice name */
  .brand { position: absolute; text-align: center; transform: translateX(-50%); white-space: nowrap; }
  .brand__dot { display: block; margin: 0 auto; border-radius: 50%; background: var(--pink); }
  .brand__tagline, .brand__name {
    display: block; font-family: "Barlow", Arial, sans-serif; font-weight: 400; color: var(--pink);
  }
  .brand__tagline { letter-spacing: .08em; }
  .brand__name { letter-spacing: .14em; text-transform: uppercase; }

  .brand--hero { left: 581px; top: 150px; }
  .brand--hero .brand__dot { width: 170px; height: 170px; margin-bottom: 80px; }
  .brand--hero .brand__tagline { font-size: 22px; line-height: 28px; margin-bottom: 6px; }
  .brand--hero .brand__name { font-size: 28px; line-height: 40px; letter-spacing: .16em; }

  .brand--small .brand__dot { width: 72px; height: 72px; margin-bottom: 16px; }
  .brand--small .brand__tagline { font-size: 10px; line-height: 12px; margin-bottom: 4px; }
  .brand--small .brand__name { font-size: 12px; line-height: 16px; }

  .brand--pad .brand__dot { width: 68px; height: 68px; margin-bottom: 14px; }
  .brand--pad .brand__tagline { font-size: 9px; line-height: 11px; margin-bottom: 2px; }
  .brand--pad .brand__name { font-size: 11px; line-height: 14px; }

  .brand--card-front .brand__dot { width: 100px; height: 100px; background: var(--emboss-light); }
  .brand--card-back .brand__tagline { font-size: 11px; line-height: 14px; margin-bottom: 46px; }
  .brand--card-back .brand__name { font-size: 13px; line-height: 16px; }

  /* presentation stage */
  .stage { position: absolute; left: 0; top: 574px; width: 1200px; height: 902px; background: var(--stage); }
  .surface {
    position: absolute; left: 0; top: 1476px; width: 1200px; height: 1222px;
    background: radial-gradient(ellipse at 70% 60%, #c2c2c2 0%, #a9a9a9 55%, #8f8f8f 100%);
  }

  .sheet { position: absolute; background: var(--paper); box-shadow: 2px 3px 8px rgba(0,0,0,.18); }
  .letter { left: 49px; width: 658px; height: 927px; }
  .letter--head { top: 670px; }
  .letter--invoice { top: 1671px; }
  .card { width: 314px; height: 189px; }
  .card--front { left: 746px; top: 670px; }
  .card--back { left: 831px; top: 853px; height: 188px; }
  .pad { left: 745px; top: 1121px; width: 399px; height: 562px; }

  .contact {
    position: absolute; left: 505px; top: 97px; padding-left: 8px; white-space: nowrap;
    border-left: 1px solid var(--rule); font-size: 10px; line-height: 12px; height: 100px;
  }
  .contact p + p { margin-top: 8px; }

  .footer-line { position: absolute; left: 0; width: 100%; text-align: center; font-size: 10px; line-height: 14px; white-space: nowrap; }
  .sep { display: inline-block; width: 1px; height: 11px; background: var(--rule); margin: 0 8px; vertical-align: -1px; }
  .tiny { font-size: 8px; }
  .tiny .sep { margin: 0 5px; height: 9px; }

  .card__role { position: absolute; left: 0; width: 100%; font-size: 10px; letter-spacing: .35em; text-align: center; }

  .label { position: absolute; font-size: 10px; white-space: nowrap; }
  .diagnose-bar { position: absolute; left: 0; top: 394px; width: 20px; height: 10px; background: var(--pink); }
  .diagnose {
    position: absolute; left: 63px; top: 388px; font-family: "Oswald", Arial, sans-serif;
    font-size: 13px; letter-spacing: .25em; color: var(--pink);
  }
  .col-head { position: absolute; top: 455px; font-size: 11px; font-weight: 600; color: var(--text-strong); }
  .col-rule { position: absolute; top: 444px; width: 1px; height: 31px; background: var(--rule); }
</style>
</head>
<body>

<div class="swatch swatch--pink"></div>
<div class="swatch swatch--grey"></div>

<div class="brand brand--hero">
  <span class="brand__dot"></span>
  <span class="brand__tagline">Homöopathische Familienpraxis</span>
  <span class="brand__name">Mareike Sonnfeld-Brandt</span>
</div>

<div class="stage"></div>
<div class="surface" role="img" aria-label="Blindgeprägtes Papier mit dem Praxiszeichen, grau strukturiert"></div>

<!-- letterhead -->
<section class="sheet letter letter--head">
  <div class="brand brand--small" style="left:152px; top:62px;">
    <span class="brand__dot"></span>
    <span class="brand__tagline">Homöopathische Familienpraxis</span>
    <span class="brand__name">Mareike Sonnfeld-Brandt</span>
  </div>
  <div class="contact">
    <p>Amselgrund 7<br>14480 Musterhain</p>
    <p>0176 555 02 718</p>
    <p>mareike@sonnfeld-post.de<br>www.sonnfeld-praxis.de</p>
  </div>
  <div class="footer-line" style="top:841px;">Nordbank Berlin<span class="sep"></span>IBAN DE 12 3456 7800 0098 7654 32<br>Steuernummer: 27/415/00362<span class="sep"></span>Umsatzsteuerbefreit nach § 4 Nr. 14a UStG</div>
</section>

<!-- business cards -->
<section class="sheet card card--front">
  <div class="brand brand--card-front" style="left:157px; top:45px;">
    <span class="brand__dot"></span>
  </div>
</section>
<section class="sheet card card--back">
  <div class="brand brand--card-back" style="left:157px; top:24px;">
    <span class="brand__tagline">Homöopathische Familienpraxis</span>
    <span class="brand__name">Mareike Sonnfeld-Brandt</span>
  </div>
  <p class="card__role" style="top:102px;">Heilpraktikerin</p>
  <div class="footer-line tiny" style="top:140px; line-height:16px;">Amselgrund 7, 14480 Musterhain<br>0176 555 02 718<span class="sep"></span>mareike@sonnfeld-post.de<span class="sep"></span>www.sonnfeld-praxis.de</div>
</section>

<!-- prescription pad -->
<section class="sheet pad">
  <div class="brand brand--pad" style="left:197px; top:26px;">
    <span class="brand__dot"></span>
    <span class="brand__tagline">Homöopathische Familienpraxis</span>
    <span class="brand__name">Mareike Sonnfeld-Brandt</span>
  </div>
  <span class="label" style="left:40px; top:178px;">Rezept</span>
  <span class="label" style="left:326px; top:178px;">Datum</span>
  <div class="footer-line tiny" style="top:501px; line-height:16px;">Amselgrund 7, 14480 Musterhain<br>0176 555 02 718<span class="sep"></span>mareike@sonnfeld-post.de<span class="sep"></span>www.sonnfeld-praxis.de</div>
</section>

<!-- invoice -->
<section class="sheet letter letter--invoice">
  <div class="brand brand--small" style="left:152px; top:62px;">
    <span class="brand__dot"></span>
    <span class="brand__tagline">Homöopathische Familienpraxis</span>
    <span class="brand__name">Mareike Sonnfeld-Brandt</span>
  </div>
  <div class="contact" style="left:510px;">
    <p>Amselgrund 7<br>14480 Musterhain</p>
    <p>0176 555 02 718</p>
    <p>mareike@sonnfeld-post.de<br>www.sonnfeld-praxis.de</p>
  </div>
  <p class="label" style="left:63px; top:226px; line-height:12px;">An<br>Max Muter<br>Beispielstrasse 4<br>1141 Samplecity</p>
  <span class="label" style="left:510px; top:283px;">Datum</span>
  <span class="label" style="left:63px; top:308px;">Für meine Bemühungen erlaube ich mir folgendes zu berechnen:</span>
  <span class="label" style="left:510px; top:309px;">R. Nummer</span>
  <div class="diagnose-bar"></div>
  <span class="diagnose">DIAGNOSE:</span>
  <span class="col-head" style="left:63px;">Datum</span>
  <span class="col-rule" style="left:146px;"></span>
  <span class="col-head" style="left:153px;">GebüH</span>
  <span class="col-rule" style="left:239px;"></span>
  <span class="col-head" style="left:249px;">Behandlung</span>
  <span class="col-rule" style="left:503px;"></span>
  <span class="col-head" style="left:510px;">Betrag in €</span>
  <div class="footer-line" style="top:843px;">Nordbank Berlin<span class="sep"></span>IBAN DE 12 3456 7800 0098 7654 32<br>Steuernummer: 27/415/00362<span class="sep"></span>Umsatzsteuerbefreit nach § 4 Nr. 14a UStG</div>
</section>

</body>
</html>
```